Halvorn spray foam and Environmental

I have business cards but need new ones. The ones I have are very bland. Here is. Y company website http://www.halvornsprayfoam.ca

Also I can send you copies of the current cards
I would also need my current logo on the new design as well.. Also spray foam and Environmental

Industry/Entity Type

Business

Logo Text

Halvorn.

```html
<!DOCTYPE html>
<html lang="en">
<head>
<meta charset="utf-8">
<title>Halvorn Business Cards</title>
<link rel="stylesheet" href="https://fonts.googleapis.com/css2?family=Jost:wght@500;600;700&family=Roboto:wght@400;500&display=swap">
<style>
  :root {
    --backdrop: #e9e6e1;
    --card: #f3f3f2;
    --purple: #6a3479;
    --green: #43c51c;
    --ink: #4a4a4a;
    --mark: #8c8a8f;
  }
  * { margin: 0; padding: 0; box-sizing: border-box; }
  html, body { width: 1200px; height: 960px; overflow: hidden; }
  body { background: var(--backdrop); position: relative; font-family: "Roboto", Arial, sans-serif; }

  .card {
    position: absolute; width: 600px; height: 343px;
    background: var(--card);
    box-shadow: 0 2px 6px rgba(0,0,0,.35);
  }
  .card--foam { left: 315px; top: 113px; }
  .card--enviro { left: 312px; top: 472px; }

  .card__band { position: absolute; left: 0; top: 0; width: 85px; height: 100%; background: var(--purple); }

  .brand { position: absolute; left: 42px; top: 54px; display: flex; align-items: flex-start; gap: 18px; }
  .card--enviro .brand { top: 41px; }
  .brand__square { width: 66px; height: 66px; background: var(--mark); border: 2px solid #fff; border-radius: 6px; margin-top: 2px; }
  .brand__name { font-family: "Jost", "Century Gothic", sans-serif; font-weight: 700; font-size: 43px; line-height: 40px; color: var(--purple); letter-spacing: 0.5px; }
  .brand__division { font-family: "Jost", "Century Gothic", sans-serif; font-weight: 600; font-size: 18px; letter-spacing: 1px; margin-top: 4px; }
  .card--foam .brand__division { color: var(--purple); }
  .card--enviro .brand__division { color: var(--green); }

  .person { position: absolute; left: 133px; top: 180px; }
  .card--enviro .person { top: 190px; }
  .person__name { font-family: "Jost", "Century Gothic", sans-serif; font-weight: 600; font-size: 23px; color: var(--purple); letter-spacing: 0.3px; line-height: 26px; }
  .person__role { font-size: 14px; font-weight: 500; margin-top: 2px; }
  .card--foam .person__role { color: var(--ink); }
  .card--enviro .person__role { color: var(--green); }

  .contact { list-style: none; margin-top: 18px; }
  .contact__item { display: flex; align-items: center; gap: 8px; font-size: 14px; color: var(--ink); line-height: 19px; height: 19px; }
  .contact__icon { width: 12px; height: 12px; fill: var(--purple); flex: none; }

  .services { position: absolute; right: 40px; top: 148px; text-align: right; }
  .card--enviro .services { top: 158px; }
  .services__title { font-family: "Jost", "Century Gothic", sans-serif; font-weight: 600; font-size: 19px; color: var(--purple); letter-spacing: 0.5px; margin-bottom: 6px; }
  .services__list { list-style: none; }
  .services__list li { font-size: 14px; color: var(--ink); line-height: 20px; }
</style>
</head>
<body>

<section class="card card--foam">
  <div class="card__band"></div>
  <div class="brand">
    <div class="brand__square"></div>
    <div>
      <div class="brand__name">HALVORN</div>
      <div class="brand__division">SPRAY FOAM LTD.</div>
    </div>
  </div>
  <div class="person">
    <div class="person__name">MAREK DALTON</div>
    <div class="person__role">CEO/FOUNDER</div>
    <ul class="contact">
      <li class="contact__item"><svg class="contact__icon" viewBox="0 0 24 24"><path d="M6.6 10.8a15 15 0 0 0 6.6 6.6l2.2-2.2c.3-.3.7-.4 1-.2 1.1.4 2.3.6 3.6.6.6 0 1 .4 1 1V20c0 .6-.4 1-1 1A17 17 0 0 1 3 4c0-.6.4-1 1-1h3.5c.6 0 1 .4 1 1 0 1.3.2 2.5.6 3.6.1.3 0 .7-.2 1z"/></svg>604-555-0172</li>
      <li class="contact__item"><svg class="contact__icon" viewBox="0 0 24 24"><path d="M2 6l10 7 10-7v13H2z M2 5h20l-10 7z"/></svg>halvornfoam@mailbox.ca</li>
      <li class="contact__item"><svg class="contact__icon" viewBox="0 0 24 24"><circle cx="12" cy="12" r="11"/><path d="M7 7c3 1 3 4 6 4s1 5 3 6M14 3c0 3 4 3 6 5" stroke="#f3f3f2" stroke-width="2" fill="none"/></svg>www.halvornsprayfoam.ca</li>
    </ul>
  </div>
  <div class="services">
    <div class="services__title">SPRAY FOAM4</div>
    <ul class="services__list">
      <li>Roofing Foam</li>
      <li>Slabjacking</li>
      <li>2 pound / Half pound</li>
      <li>Sound Proofing</li>
      <li>Batt insulation</li>
      <li>Attic Blow in</li>
    </ul>
  </div>
</section>

<section class="card card--enviro">
  <div class="card__band"></div>
  <div class="brand">
    <div class="brand__square"></div>
    <div>
      <div class="brand__name">HALVORN</div>
      <div class="brand__division">ENVIRONMENTAL</div>
    </div>
  </div>
  <div class="person">
    <div class="person__name">MAREK DALTON</div>
    <div class="person__role">CEO/FOUNDER</div>
    <ul class="contact">
      <li class="contact__item"><svg class="contact__icon" viewBox="0 0 24 24"><path d="M6.6 10.8a15 15 0 0 0 6.6 6.6l2.2-2.2c.3-.3.7-.4 1-.2 1.1.4 2.3.6 3.6.6.6 0 1 .4 1 1V20c0 .6-.4 1-1 1A17 17 0 0 1 3 4c0-.6.4-1 1-1h3.5c.6 0 1 .4 1 1 0 1.3.2 2.5.6 3.6.1.3 0 .7-.2 1z"/></svg>604-555-0148</li>
      <li class="contact__item"><svg class="contact__icon" viewBox="0 0 24 24"><path d="M2 6l10 7 10-7v13H2z M2 5h20l-10 7z"/></svg>greenwork@mailbox.ca</li>
      <li class="contact__item"><svg class="contact__icon" viewBox="0 0 24 24"><circle cx="12" cy="12" r="11"/><path d="M7 7c3 1 3 4 6 4s1 5 3 6M14 3c0 3 4 3 6 5" stroke="#f3f3f2" stroke-width="2" fill="none"/></svg>www.halvornenvironmental.ca</li>
    </ul>
  </div>
  <div class="services">
    <div class="services__title">ENVIRONMENTAL</div>
    <ul class="services__list">
      <li>air monitoring</li>
      <li>Asbestos testing</li>
      <li>Asbestos Removal</li>
      <li>Building Demolition</li>
      <li>Lead Testing</li>
      <li>Mould Removal</li>
    </ul>
  </div>
</section>

</body>
</html>
```